Catholic Musical composer/producer needs poster for groundbreaking new musical, "Harvest of Velmont

We need a dynamic poster for "Harvest of Velmont," a new musical written for Catholic dinner theater. Looking for that iconic poster graphic like you see in posters for classic musicals, like "Nuit Dorée," Carousel of Lanterns," or "Spindle."
***

"Harvest of Velmont" is based on the Gospel of John 2:1-11 where Jesus performs his first miracle at the behest of His Mother, Mary. It takes place at a wedding where the host family runs out of wine, a huge embarrassment. Mary becomes aware of the problem and directs Jesus to intercede. Jesus directs the wine steward to fill 6 large 30 gallon jars with water. He prays over them, turning the water into wine. The chalice of wine is a symbol for the Eucharist (communion). Even more, the Blood of Christ (the wine) is the source of spiritual life. Poster text is found on attachment.

Target Market(s)

The audience is adult members of Catholic churches. Don't want design to look too "churchy."

Industry/Entity Type

Wedding

Colors

Designer to choose colors to be used in the design.

Requirements
Must have
• Photoshop with layers, or vector format.

Looking for that iconic poster graphic like you see in posters for classic musicals, like "Nuit Dorée," Carousel of Lanterns," or "Spindle."
Should not have
• Really don't want photos.

```html
<!DOCTYPE html>
<html lang="en">
<head>
<meta charset="utf-8">
<title>Harvest of Velmont</title>
<link rel="stylesheet" href="https://fonts.googleapis.com/css2?family=Cinzel:wght@400;600&family=Fondamento:ital@1&display=swap">
<style>
  :root {
    --night: #04040e;
    --rose-deep: #5a0208;
    --rose: #b3101a;
    --rose-bright: #e0262c;
    --silver-light: #ffffff;
    --silver-mid: #d9d8cc;
    --silver-dark: #8d8c7c;
    --gold: #d8b13e;
    --gold-soft: #c9a13a;
    --ink: #ffffff;
  }
  * { margin: 0; padding: 0; box-sizing: border-box; }
  html, body { width: 899px; height: 1200px; overflow: hidden; background: var(--night); }
  .poster {
    position: relative;
    width: 899px;
    height: 1200px;
    background: var(--night);
    overflow: hidden;
    font-family: "Cinzel", serif;
    color: var(--ink);
  }
  .rose-art {
    position: absolute;
    left: 0; top: 0;
    width: 899px; height: 820px;
  }
  .title {
    position: absolute;
    left: 0; width: 870px;
    top: 165px;
    text-align: center;
    font-weight: 400;
    line-height: 1;
    background: linear-gradient(180deg, var(--silver-light) 0%, var(--silver-mid) 55%, var(--silver-dark) 100%);
    -webkit-background-clip: text;
    background-clip: text;
    color: transparent;
    text-shadow: 0 0 1px rgba(255,255,255,0.05);
  }
  .title-line { display: block; }
  .title-main { font-size: 104px; letter-spacing: 1px; }
  .title-small { font-size: 60px; margin: 10px 0 6px; }
  .divider {
    position: absolute;
    left: 50%;
    transform: translateX(-50%);
  }
  .divider-top { top: 500px; left: 435px; width: 560px; }
  .divider-bottom { top: 1050px; left: 435px; width: 380px; }
  .tagline {
    position: absolute;
    left: 0; width: 870px;
    text-align: center;
    color: var(--gold);
  }
  .tagline-script {
    top: 572px;
    font-family: "Fondamento", cursive;
    font-style: italic;
    font-size: 25px;
  }
  .tagline-psalm {
    top: 620px;
    font-size: 27px;
    font-weight: 600;
  }
  .tagline-motto {
    top: 678px;
    font-family: "Fondamento", cursive;
    font-style: italic;
    font-size: 18px;
    word-spacing: 8px;
    color: var(--gold-soft);
  }
  .event-details {
    position: absolute;
    top: 812px;
    left: 0; width: 870px;
    list-style: none;
    text-align: center;
    font-size: 20px;
    line-height: 30px;
  }
  .ticket-note {
    position: absolute;
    top: 1002px;
    left: 0; width: 870px;
    text-align: center;
    font-size: 21px;
  }
</style>
</head>
<body>
<div class="poster">
  <svg class="rose-art" viewBox="0 0 899 820" role="img" aria-label="Photograph of a cluster of deep red roses framing the upper right of the poster">
    <defs>
      <radialGradient id="roseGlow" cx="0.72" cy="0.38" r="0.7">
        <stop offset="0" stop-color="var(--rose-bright)"/>
        <stop offset="0.55" stop-color="var(--rose)"/>
        <stop offset="1" stop-color="var(--rose-deep)"/>
      </radialGradient>
    </defs>
    <path d="M240 0 H899 V800 Q800 830 690 790 Q660 700 640 640 Q580 560 610 470 Q560 420 590 340 Q560 260 610 190 Q560 160 520 150 Q400 170 300 140 Q245 90 240 0 Z" fill="url(#roseGlow)"/>
  </svg>

  <h1 class="title">
    <span class="title-line title-main">Harvest</span>
    <span class="title-line title-small">of</span>
    <span class="title-line title-main">Velmont</span>
  </h1>

  <svg class="divider divider-top" viewBox="0 0 560 24" aria-hidden="true">
    <defs>
      <linearGradient id="lineFadeTop" x1="0" x2="1">
        <stop offset="0" stop-color="#ffffff" stop-opacity="0"/>
        <stop offset="0.5" stop-color="#ffffff"/>
        <stop offset="1" stop-color="#ffffff" stop-opacity="0"/>
      </linearGradient>
    </defs>
    <rect x="0" y="11" width="235" height="2" fill="url(#lineFadeTop)"/>
    <rect x="325" y="11" width="235" height="2" fill="url(#lineFadeTop)"/>
    <ellipse cx="280" cy="12" rx="38" ry="9" fill="#d9d8cc" role="img" aria-label="Small silver flourish ornament"/>
  </svg>

  <p class="tagline tagline-script">The new musical for Catholic Dinner Theater</p>
  <p class="tagline tagline-psalm">Taste and see the goodness of the Lord!</p>
  <p class="tagline tagline-motto">Wine. Passion. Life!</p>

  <ul class="event-details">
    <li>[Where: [church name</li>
    <li>Date:</li>
    <li>Time:</li>
    <li>Ticket prices:</li>
  </ul>

  <p class="ticket-note">Ticket price includes show/dinner/wine</p>

  <svg class="divider divider-bottom" viewBox="0 0 380 24" aria-hidden="true">
    <defs>
      <linearGradient id="lineFadeBottom" x1="0" x2="1">
        <stop offset="0" stop-color="#ffffff" stop-opacity="0"/>
        <stop offset="0.5" stop-color="#ffffff"/>
        <stop offset="1" stop-color="#ffffff" stop-opacity="0"/>
      </linearGradient>
    </defs>
    <rect x="0" y="11" width="145" height="2" fill="url(#lineFadeBottom)"/>
    <rect x="235" y="11" width="145" height="2" fill="url(#lineFadeBottom)"/>
    <ellipse cx="190" cy="12" rx="38" ry="9" fill="#d9d8cc" role="img" aria-label="Small silver flourish ornament"/>
  </svg>
</div>
</body>
</html>
```